Do it yourself blood pressure poster and flyer

I work in a Drs Health Centre. We have a pod where patients can do their own blood pressure, height, weight etc. We'd like to design a poster and a flyer to encourage patients to use it. The poster would be on display in the waiting room and the flyer would be given to patients. Once in the pod, the measurements are easy to do and take less than 5 minutes.
Our name is Pencoedwyn Health Centre

Target Market(s)

Patinets in a deprived area, UK

Industry/Entity Type

Health Care

Requirements
Must have
• Eye catching; encourage patients to use self measurement of blood pressure
Nice to have
• Not too serious. Only takes a few minutes. Give result to Receptionist or Dr

```html
<!DOCTYPE html>
<html lang="en">
<head>
<meta charset="utf-8">
<title>Pencoedwyn Health Centre – Self Measurement of Blood Pressure</title>
<link rel="stylesheet" href="https://fonts.googleapis.com/css2?family=Raleway:wght@400;700&display=swap">
<style>
  :root {
    --page-bg: #e4e4e4;
    --poster-bg: #f3f3f3;
    --coral: #ec6a55;
    --coral-soft: #f08a77;
    --rose: #c9667e;
    --sky: #5ab8f0;
    --sky-deep: #3aa6ec;
    --steel: #6a8fc4;
    --title-blue: #3d8fdc;
    --subtitle-blue: #5f9fd8;
    --ink: #1f3a52;
  }
  * { margin: 0; padding: 0; box-sizing: border-box; }
  html, body { width: 1200px; height: 1200px; overflow: hidden; }
  body { background: var(--page-bg); position: relative; }

  .poster {
    position: absolute;
    left: 190px; top: 20px;
    width: 820px; height: 1160px;
    background: var(--poster-bg);
    overflow: hidden;
  }
  .poster-art { position: absolute; inset: 0; width: 820px; height: 1160px; }

  .brand {
    position: absolute;
    left: 166px; top: 50px;
    font-family: "Raleway", sans-serif;
    font-weight: 700;
    color: var(--title-blue);
    font-size: 55px;
    line-height: 54px;
    letter-spacing: 3px;
  }
  .headline {
    position: absolute;
    left: 55px; top: 201px;
    font-family: "Raleway", sans-serif;
    font-weight: 400;
    color: var(--subtitle-blue);
    font-size: 31px;
    line-height: 39px;
    letter-spacing: 1.2px;
  }
</style>
</head>
<body>
<main class="poster">
  <svg class="poster-art" viewBox="279 74 944 1336" preserveAspectRatio="none" xmlns="http://www.w3.org/2000/svg">
    <defs>
      <linearGradient id="coral-fade" x1="0" y1="0" x2="1" y2="0">
        <stop offset="0" stop-color="#c8677f"/>
        <stop offset="1" stop-color="#f08a77"/>
      </linearGradient>
      <linearGradient id="coral-deep" x1="0" y1="0" x2="1" y2="0">
        <stop offset="0" stop-color="#c65f79"/>
        <stop offset="1" stop-color="#ec6a55"/>
      </linearGradient>
      <linearGradient id="blend-fade" x1="0" y1="0" x2="1" y2="0">
        <stop offset="0" stop-color="#c28a9a" stop-opacity="0.85"/>
        <stop offset="1" stop-color="#5aa8e6" stop-opacity="0.95"/>
      </linearGradient>
      <linearGradient id="sky-fade" x1="0" y1="0" x2="1" y2="1">
        <stop offset="0" stop-color="#6cc0f2"/>
        <stop offset="1" stop-color="#3ab0f0"/>
      </linearGradient>
      <linearGradient id="sky-low" x1="0" y1="0" x2="1" y2="0">
        <stop offset="0" stop-color="#7fb0e2"/>
        <stop offset="1" stop-color="#5ab8f0"/>
      </linearGradient>
      <linearGradient id="wrist-photo" x1="0" y1="0" x2="1" y2="1">
        <stop offset="0" stop-color="#e9d7c6"/>
        <stop offset="0.5" stop-color="#f2f2f2"/>
        <stop offset="1" stop-color="#8a8e92"/>
      </linearGradient>
      <linearGradient id="patient-photo" x1="0" y1="0" x2="1" y2="1">
        <stop offset="0" stop-color="#f4f4f6"/>
        <stop offset="0.5" stop-color="#e6c9b3"/>
        <stop offset="1" stop-color="#f1f1f1"/>
      </linearGradient>
      <linearGradient id="feet-photo" x1="0" y1="0" x2="0" y2="1">
        <stop offset="0" stop-color="#d9a98d"/>
        <stop offset="1" stop-color="#ececec"/>
      </linearGradient>
    </defs>

    <!-- background facets -->
    <rect class="backdrop" x="279" y="74" width="944" height="1336" fill="#f3f3f3"/>
    <polygon points="279,250 520,74 700,420" fill="#ececec"/>
    <polygon points="780,300 1223,180 1223,560" fill="#e9e9e9"/>
    <polygon points="279,1100 560,1410 279,1410" fill="#ededed"/>
    <polygon points="600,1150 900,1410 500,1410" fill="#efefef"/>

    <!-- corner decorations -->
    <g role="img" aria-label="Scattered pill and stethoscope decoration">
      <rect x="279" y="74" width="60" height="60" rx="10" fill="#f0c9bc" opacity="0.45"/>
      <rect x="279" y="190" width="60" height="120" rx="10" fill="#c7d3dc" opacity="0.45"/>
    </g>
    <g role="img" aria-label="Stethoscope and pill decoration">
      <rect x="1020" y="80" width="200" height="170" rx="20" fill="#d3dde6" opacity="0.45"/>
    </g>

    <!-- brand mark -->
    <circle class="brand-dot" cx="382" cy="193" r="56" fill="var(--coral)"/>

    <!-- hexagon mosaic -->
    <polygon points="330,477 486,567 486,745 330,835 174,745 174,567" fill="url(#coral-fade)"/>
    <polygon points="330,655 486,745 486,923 330,1013 174,923 174,745" fill="url(#coral-deep)" opacity="0.75"/>
    <polygon points="330,1030 486,1120 486,1298 330,1388 174,1298 174,1120" fill="url(#coral-deep)"/>
    <polygon points="430,1195 495,1232 495,1308 430,1345 365,1308 365,1232" fill="#ec6a55" opacity="0.85"/>

    <polygon points="800,760 956,850 956,1030 800,1120 644,1030 644,850" fill="url(#blend-fade)"/>
    <polygon points="795,1025 880,1075 880,1225 795,1275 710,1225 710,1075" fill="#8f8fb5" opacity="0.7"/>

    <polygon points="1118,502 1281,596 1281,784 1118,878 955,784 955,596" fill="url(#sky-fade)"/>
    <polygon points="1118,760 1281,850 1281,1030 1118,1120 955,1030 955,850" fill="url(#sky-fade)" opacity="0.85"/>
    <polygon points="960,1040 1116,1130 1116,1310 960,1400 804,1310 804,1130" fill="url(#sky-low)" opacity="0.9"/>
    <polygon points="1200,1230 1280,1276 1280,1370 1200,1416 1120,1370 1120,1276" fill="#5ab8f0"/>

    <g role="img" aria-label="Photo: wrist blood pressure monitor being worn">
      <polygon points="644,477 803,569 803,751 644,843 485,751 485,569" fill="url(#wrist-photo)"/>
    </g>
    <g role="img" aria-label="Photo: smiling patient giving a thumbs up while wearing a wrist monitor">
      <polygon points="484,755 645,848 645,1032 484,1125 323,1032 323,848" fill="url(#patient-photo)"/>
    </g>
    <g role="img" aria-label="Photo: bare feet on bathroom scales">
      <polygon points="946,517 1012,555 1012,630 946,668 880,630 880,555" fill="url(#feet-photo)"/>
    </g>
    <g role="img" aria-label="Photo: bare feet standing on weighing scales">
      <polygon points="1118,1030 1278,1122 1278,1306 1118,1398 958,1306 958,1122" fill="url(#feet-photo)"/>
    </g>
  </svg>

  <h1 class="brand">PENCOEDWYN<br>HEALTH CENTRE</h1>
  <p class="headline">We Encourage Patients to Use Self<br>Measurement of Blood Pressure</p>
</main>
</body>
</html>
```